Postcard Design

We are a line of nourishing personal care products. We have recently revamped our look and want the postcard to show our new look, with pics and logo and remind customers what kind of products we make. We like clean, white, pretty, apathetic look. Obviously doesn't have to include all the pics. Just wanted to have some different looks to choose from, but would like a few.

Target Market(s)

boutique stores, spas, upscale lady.

Requirements
Must have
• Our pantry of goodies include: Silk Body Whips, Sugar Polish, Salt Polish, Silk Body Washes, Hand and Foot creams, Parisian Hair Balm, Bubbles, and much more.

Many fabulous aroma blends to choose from such as: Citrus, Sea Glass, Birch, Lavender Sage, Mango Wit Da Guava, Green Cedar, Chamomile Bloom, Pink Peony, Lily, Vanilla Fig, Cream, and Sea Breeze.

For more information or to order: velorabotanica.com; 800.417.3962; or info@velorabotanica.com

Return address: 518 Birchell Ave Dayton Oh 45873

```html
<!DOCTYPE html>
<html lang="en">
<head>
<meta charset="utf-8">
<title>Velora Botanica Postcard</title>
<link rel="stylesheet" href="https://fonts.googleapis.com/css2?family=Crimson+Text:wght@400;700&family=Libre+Baskerville:ital,wght@0,400;0,700;1,400&display=swap">
<style>
  :root {
    --maroon: #8c2a33;
    --band: #a0323b;
    --ink: #2a2526;
    --frame: #3a3a3a;
    --paper: #ffffff;
    --pattern: #f6ecec;
    --white: #ffffff;
  }
  * { margin: 0; padding: 0; box-sizing: border-box; }
  html, body { width: 1200px; height: 918px; overflow: hidden; background: var(--paper); }
  .postcard {
    position: relative;
    width: 1200px; height: 918px;
    background: var(--paper);
    font-family: "Crimson Text", Georgia, serif;
    color: var(--ink);
  }
  .postcard__frame {
    position: absolute; left: 14px; top: 12px; width: 1171px; height: 893px;
    border: 3px solid var(--frame);
  }
  .postcard__pattern {
    position: absolute; left: 17px; top: 15px; width: 1165px; height: 450px;
    background: radial-gradient(ellipse at center, var(--paper) 30%, var(--pattern) 100%);
  }
  .brand-name {
    position: absolute; left: 0; right: 0; top: 20px;
    text-align: center;
    font-weight: 700; font-size: 104px; line-height: 1; letter-spacing: 4px;
    color: var(--maroon);
  }
  .section-heading {
    position: absolute; left: 0; right: 0; text-align: center;
    font-family: "Libre Baskerville", Georgia, serif;
    font-weight: 700; color: var(--ink); line-height: 1;
  }
  .section-heading--pantry { top: 150px; font-size: 32px; }
  .section-heading--aromas { top: 296px; font-size: 31px; letter-spacing: -0.5px; }
  .item-list {
    position: absolute; left: 0; right: 0; text-align: center;
    font-size: 33px; line-height: 39px; color: var(--ink);
  }
  .item-list--pantry { top: 186px; }
  .item-list--aromas { top: 332px; }
  .photo {
    position: absolute; top: 466px; height: 260px;
  }
  .photo--washes {
    left: 33px; width: 546px;
    background: linear-gradient(180deg, #eeeeee 0%, #f7f5f2 55%, #e9e7e3 100%);
  }
  .photo--bath {
    left: 598px; width: 546px;
    background: linear-gradient(180deg, #ece9e6 0%, #f1efec 55%, #d9d3cc 100%);
  }
  .contact-band {
    position: absolute; left: 17px; top: 744px; width: 1165px; height: 158px;
    background: var(--band);
    color: var(--white); text-align: center;
    font-family: "Libre Baskerville", Georgia, serif;
    font-weight: 700; line-height: 1;
  }
  .contact-band__lead {
    position: absolute; left: 0; right: 0; top: 12px;
    font-style: italic; font-size: 25px;
  }
  .contact-band__details {
    position: absolute; left: 0; right: 0; top: 50px;
    font-size: 25px;
  }
  .contact-band__details span + span { margin-left: 32px; }
  .contact-band__address {
    position: absolute; left: 0; right: 0; top: 92px;
    font-size: 31px;
  }
</style>
</head>
<body>
<main class="postcard">
  <div class="postcard__pattern" role="img" aria-label="Soft pale pink lattice background pattern"></div>

  <h1 class="brand-name">Velora Botanica</h1>

  <h2 class="section-heading section-heading--pantry">Our Pantry of Goodies Include:</h2>
  <p class="item-list item-list--pantry">
    Silk Body Whips • Sugar Polish • Salt Polish • Silk Body Washes<br>
    Hand and Foot Creams • Parisian Hair Balm • Bubbles and much more
  </p>

  <h2 class="section-heading section-heading--aromas">Many Fabulous Aroma Blends to Choose From Such As:</h2>
  <p class="item-list item-list--aromas">
    Citrus • Sea Glass • Birch • Lavender Sage<br>
    Mango Wit Da Guava • Green Cedar • Chamomile Bloom<br>
    Pink Peony • &nbsp;Lily • Vanilla Fig • Cream and Sea Breeze
  </p>

  <div class="photo photo--washes" role="img" aria-label="Photo of five body wash bottles with pastel labels in a row"></div>
  <div class="photo photo--bath" role="img" aria-label="Photo of a white clawfoot tub with blossoms, bunting and jars of body products"></div>

  <footer class="contact-band">
    <p class="contact-band__lead">For more information or to order</p>
    <p class="contact-band__details"><span>velorabotanica.com</span><span>800.417.3962</span><span>or info@velorabotanica.com</span></p>
    <p class="contact-band__address">Return Address: 518 Birchell Ave Brenton, OH 45873</p>
  </footer>

  <div class="postcard__frame"></div>
</main>
</body>
</html>
```